House Builder and Property Development Card Design and Logo

I need a business card design for a building and property development company.
Colour scheme of Dark Grey and Green, I would like it bold, sharp and professional.
No logo yet done, I'm open to options but please stay away from the usual- house, roof, hammers etc.
Thanks Rob

Please be aware that on the business card information section the WHRC # 5528391 is a licence number and my phone number 0492837165. The numbers are close together and could be mistaken as one whole number 

Thank you

                                   

Industry/Entity Type

Building

Contact Information for Business Card

VARGA BUILD & DEVELOPMENT.
Residential Building & Property Development
Robert Varga - Director
WHRC # 5528391
0492837165
rob@vargabuild.example.com.au

Requirements
Must have
• Bold Business name
Dark grey and green colours
Should not have
• roof outline or hammer logo

```html
<!DOCTYPE html>
<html lang="en">
<head>
<meta charset="utf-8">
<title>Varga Build &amp; Development – Business Card</title>
<link rel="stylesheet" href="https://fonts.googleapis.com/css2?family=Open+Sans:wght@400;700&family=Roboto:wght@400&display=swap">
<style>
  :root {
    --canvas: #ffffff;
    --card-border: #4a4a4a;
    --frame-border: #cfcfcf;
    --ink-grey: #5f5f60;
    --label-ink: #333333;
    --band-green: #118a4e;
    --band-grey: #5f5f60;
  }
  * { margin: 0; padding: 0; box-sizing: border-box; }
  html, body { width: 1200px; height: 900px; overflow: hidden; background: var(--canvas); }
  .sheet {
    position: relative;
    width: 1200px; height: 900px;
    border: 1px solid var(--frame-border);
  }
  .side-label {
    position: absolute;
    font-family: "Roboto", Arial, sans-serif;
    font-size: 22px;
    color: var(--label-ink);
    transform: translateX(-50%);
  }
  .side-label--front { left: 301px; top: 250px; }
  .side-label--back { left: 900px; top: 253px; }
  .card {
    position: absolute;
    top: 279px;
    width: 596px; height: 368px;
    border: 1px solid var(--card-border);
    background: var(--canvas);
    overflow: hidden;
  }
  .card--front { left: 3px; }
  .card--back { left: 602px; }
  .card__band { position: absolute; left: 0; bottom: 0; width: 100%; height: 50px; }
  .company-name {
    position: absolute;
    left: 0; right: 0; top: 162px;
    text-align: center;
    font-family: "Open Sans", Arial, sans-serif;
    font-weight: 700;
    font-size: 23.5px;
    letter-spacing: 0;
    color: var(--ink-grey);
  }
  .contact {
    position: absolute;
    left: 0; right: 0; top: 149px;
    text-align: center;
    font-family: "Open Sans", Arial, sans-serif;
    font-style: normal;
    font-size: 14.5px;
    line-height: 19px;
    color: var(--ink-grey);
  }
  .contact__sep { display: inline-block; margin: 0 8px; }
  .band-back { background: var(--band-grey); }
</style>
</head>
<body>
  <main class="sheet">
    <div class="side-label side-label--front">Front</div>
    <div class="side-label side-label--back">Back</div>

    <section class="card card--front">
      <h1 class="company-name">VARGA BUILD &amp; DEVELOPMENT.</h1>
      <svg class="card__band" viewBox="0 0 596 50" preserveAspectRatio="none" aria-hidden="true">
        <rect x="0" y="0" width="596" height="50" fill="var(--band-grey)"/>
        <polygon points="0,0 455,0 488,50 0,50" fill="var(--band-green)"/>
        <line x1="457" y1="0" x2="490" y2="50" stroke="#ffffff" stroke-width="3"/>
      </svg>
    </section>

    <section class="card card--back">
      <address class="contact">
        <div class="contact__tagline">Residential Building &amp; Property Development</div>
        <div class="contact__name">Robert Varga - Director</div>
        <div class="contact__details">WHRC # 5528391<span class="contact__sep">|</span>0492837165<span class="contact__sep">|</span>rob@vargabuild.example.com.au</div>
      </address>
      <div class="card__band band-back"></div>
    </section>
  </main>
</body>
</html>
```